Patient "menu"/catalog for IV Therapy spa

We have a "menu" that's basically just a bunch of Word documents explaining what we do and what's in each package, but it's weak. We had the pages laminated and bound at Desk Harbor and they look like crap. I also need to add information and be able to edit the pages. We HAVE to print the "catalog" with Printwell and want the size to be 5.5"x8.5" and glossy. We're imagining our logo on the front page, some "what to expect" and "what we're all about" info on the inside cover, and then each IV package and injection will have its own page. We can start with the copy that's currently on our menu, but we need to add some things to several of the pages. Things change all the time in this industry, and we're expanding regularly, so we have to have the ability to alter and reprint. I'm attaching some of the current files.

Target Market(s)

Current patients

Industry/Entity Type

Medical

Font styles to use
Other font styles liked:
• Whatever is on our bifold brochure would be fine.

Colors
0094D4
00A9DD
6FCCEA
C7EBF8
E9F6FB
00AB8E
00BBA5
67D7C9
C6EFE9
E9F9F6

Requirements
Must have
• 5.5:x8.5", printable at Printwell. Must be two-sided and editable by us for future changes
Nice to have
• Gotta be glossy and cool, but professional.
Should not have
• Stock images that we don't provide

```html
<!DOCTYPE html>
<html lang="en">
<head>
<meta charset="utf-8">
<title>Injections – Swift Revive</title>
<link rel="stylesheet" href="https://fonts.googleapis.com/css2?family=Poppins:wght@400;600;700&family=Roboto:wght@500;700&display=swap">
<style>
  :root {
    --teal: #137a8c;
    --ink: #1d1d1d;
    --paper: #f3f4f4;
    --backdrop: #e8e8e8;
    --badge: #b9b9b9;
  }
  * { box-sizing: border-box; margin: 0; padding: 0; }
  html, body { width: 981px; height: 1200px; overflow: hidden; background: var(--backdrop); }
  .page {
    position: absolute; left: 102px; top: 0; width: 776px; height: 1200px;
    background: radial-gradient(circle at 30% 20%, #fafafa, var(--paper) 70%);
    font-family: "Poppins", sans-serif; color: var(--ink);
  }
  .page-title {
    position: absolute; left: 62px; top: 44px;
    font-family: "Roboto", sans-serif; font-weight: 700; font-size: 33px;
    color: var(--teal); letter-spacing: -0.5px;
  }
  .hero-photo {
    position: absolute; left: 62px; top: 106px; width: 371px; height: 299px;
    background: linear-gradient(135deg, #f2f2f2, #e4e4e4 70%, #dcdcdc);
  }
  .hero-panel {
    position: absolute; left: 433px; top: 94px; width: 310px; height: 311px;
    background: var(--teal);
  }
  .hero-frame {
    position: absolute; left: 403px; top: 180px; width: 292px; height: 161px;
    border: 1px solid #fff;
  }
  .hero-copy {
    position: absolute; left: 454px; top: 189px;
    font-family: "Roboto", sans-serif; font-weight: 700; font-size: 18px;
    line-height: 24.4px; color: #fff; text-transform: uppercase; white-space: nowrap;
  }
  .hero-price {
    position: absolute; left: 500px; top: 347px;
    font-weight: 700; font-size: 49px; color: #fff; line-height: 1;
  }
  .hero-price sup { font-size: 22px; vertical-align: top; position: relative; top: 2px; }
  .item-art { position: absolute; }
  .art-b12 {
    left: 114px; top: 455px; width: 101px; height: 149px;
    border-radius: 50% 50% 50% 50% / 38% 38% 62% 62%;
    background: radial-gradient(circle at 45% 60%, #f59a3a, #e26a12 75%);
  }
  .art-sun { left: 60px; top: 631px; width: 194px; height: 156px;
    background: radial-gradient(circle at 35% 60%, #fff1a8, #e3a21a 30%, #7a4a06 85%); }
  .art-vial { left: 81px; top: 829px; width: 139px; height: 198px;
    border-radius: 10px 10px 14px 14px;
    background: linear-gradient(90deg, #6a2f08, #b8601c 45%, #7a3a0c); }
  .item-copy {
    position: absolute; left: 285px;
    font-size: 17px; line-height: 21.2px; white-space: nowrap;
  }
  .item-copy p + p { margin-top: 21px; }
  .item-copy strong { font-weight: 600; }
  .copy-b12 { top: 472px; }
  .copy-vitd { top: 623px; left: 283px; }
  .copy-amino { top: 845px; }
  .more-link {
    position: absolute; left: 285px; top: 1033px;
    font-weight: 600; font-size: 17px; color: var(--teal);
  }
  .brand {
    position: absolute; left: 62px; top: 1114px;
    display: flex; align-items: center; gap: 10px;
  }
  .brand-mark { width: 14px; height: 14px; border-radius: 50%; background: var(--teal); }
  .brand-name {
    font-weight: 400; font-size: 27px; color: var(--teal); line-height: 1;
  }
  .site-pill {
    position: absolute; left: 466px; top: 1115px; width: 226px; height: 31px;
    background: var(--teal);
    clip-path: polygon(10px 0, 100% 0, 100% 100%, 0 100%);
    color: #fff; font-size: 12.5px; line-height: 31px; padding-left: 19px;
  }
  .page-number {
    position: absolute; left: 677px; top: 1108px; width: 41px; height: 41px; border-radius: 50%;
    background: var(--badge); color: #fff; font-weight: 700; font-size: 15px;
    line-height: 41px; text-align: center;
  }
</style>
</head>
<body>
<main class="page">
  <h1 class="page-title">INJECTIONS</h1>

  <div class="hero-photo" role="img" aria-label="Glass vial and syringe on a white background"></div>
  <div class="hero-panel"></div>
  <div class="hero-frame"></div>
  <p class="hero-copy">Sometimes you don’t<br>need all the fluids<br>and meds, and just a<br>little boost will do.<br>That’s why we offer<br>select injections.</p>
  <p class="hero-price"><sup>$</sup>35-40</p>

  <div class="item-art art-b12" role="img" aria-label="Orange droplet labelled Vitamin B12"></div>
  <div class="item-copy copy-b12">
    <p><strong>B12</strong> is the perfect natural quick pick-me-up.</p>
    <p>You aren’t going to want this after about 6 at night,<br>unless you work the late shift. Better for you than<br>an energy drink, and will last longer as well.</p>
  </div>

  <div class="item-art art-sun" role="img" aria-label="Silhouette holding a glowing sun against a golden sky"></div>
  <div class="item-copy copy-vitd">
    <p><strong>Vitamin D</strong> is critical for platelet and blood<br>formation, and calcium absorption, which<br>assures bone health. Over 1 billion people<br>worldwide are Vitamin D deficient.</p>
    <p>If you’re feeling draggy or anemic, this Syringe of<br>Sunshine might do the trick.</p>
  </div>

  <div class="item-art art-vial" role="img" aria-label="Amber injection vial of amino acid blend"></div>
  <div class="item-copy copy-amino">
    <p><strong>Amino Blend</strong> is a powerful blend of amino acids<br>(ornithine, arginine, citruline) designed for a<br>pre-athletic boost, and post-event muscle<br>recovery. Ask us for more details.</p>
    <p>Please check with your governing body before<br>receiving a TriBlend injection. Not allowed<br>by all sports.</p>
  </div>
  <p class="more-link">More injections available</p>

  <div class="brand">
    <span class="brand-mark"></span>
    <p class="brand-name">Swift Revive</p>
  </div>

  <div class="site-pill">www.swiftreviveroom.com</div>
  <div class="page-number">14</div>
</main>
</body>
</html>
```